Stationery Design for a fast food resturaunt

We just created our logo, we need nice stationary to go with it. We beed the design to be on white background and black background.

Target Market(s)

Landlords who will lease their retail shops to us. Shopping Mall Management.Real Estate Professionals.

Font styles to use
Sans Serif

```html
<!DOCTYPE html>
<html lang="en">
<head>
<meta charset="utf-8">
<title>Amber Hive — Business Card</title>
<link href="https://fonts.googleapis.com/css2?family=Open+Sans:ital,wght@0,300;0,400;1,400&display=swap" rel="stylesheet">
<style>
  :root {
    --page-bg: #e9e9ea;
    --card-dark: #2b2b2c;
    --card-light: #4b4b4c;
    --gold: #d9a42b;
    --muted-grey: #55575a;
  }
  * { margin: 0; padding: 0; box-sizing: border-box; }
  html, body {
    width: 1200px;
    height: 1070px;
    overflow: hidden;
    background: var(--page-bg);
    font-family: "Open Sans", Arial, sans-serif;
  }
  .sheet {
    width: 1200px;
    height: 1070px;
    display: flex;
    flex-direction: column;
    align-items: center;
    justify-content: center;
    gap: 40px;
  }
  .card {
    width: 820px;
    height: 469px;
    background: linear-gradient(120deg, var(--card-dark) 0%, var(--card-dark) 35%, var(--card-light) 100%);
    position: relative;
    color: var(--gold);
    box-shadow: 0 6px 18px rgba(0,0,0,0.18);
  }

  /* Wordmark set in the text font */
  .wordmark {
    display: flex;
    align-items: center;
    gap: 18px;
    font-weight: 300;
    letter-spacing: 0.06em;
    color: var(--gold);
    white-space: nowrap;
  }
  .wordmark__square {
    background: var(--gold);
    flex: none;
  }

  /* Front */
  .card--front {
    display: flex;
    align-items: center;
    justify-content: center;
  }
  .card--front .wordmark { font-size: 72px; }
  .card--front .wordmark__square { width: 34px; height: 34px; }

  /* Back */
  .card--back { display: flex; }
  .card__brand {
    width: 47%;
    display: flex;
    align-items: center;
    justify-content: center;
  }
  .card--back .wordmark { font-size: 36px; gap: 12px; }
  .card--back .wordmark__square { width: 18px; height: 18px; }
  .card__divider {
    width: 1px;
    background: var(--gold);
    opacity: 0.7;
    margin: 40px 0;
  }
  .card__contact {
    flex: 1;
    padding: 84px 0 0 44px;
  }
  .contact__name {
    font-size: 26px;
    font-weight: 400;
    letter-spacing: 0.02em;
  }
  .contact__title {
    font-size: 19px;
    font-style: italic;
    margin: 2px 0 0 18px;
  }
  .contact__list {
    list-style: none;
    margin-top: 34px;
    font-size: 19px;
  }
  .contact__item {
    display: flex;
    align-items: center;
    gap: 12px;
    margin-bottom: 8px;
  }
  .contact__icon { width: 18px; height: 18px; fill: var(--gold); flex: none; }
</style>
</head>
<body>
<main class="sheet">

  <section class="card card--front" aria-label="Card front">
    <div class="wordmark">
      <span>AMBER HIVE</span>
      <span class="wordmark__square"></span>
    </div>
  </section>

  <section class="card card--back" aria-label="Card back">
    <div class="card__brand">
      <div class="wordmark">
        <span>AMBER HIVE</span>
        <span class="wordmark__square"></span>
      </div>
    </div>
    <div class="card__divider"></div>
    <div class="card__contact">
      <p class="contact__name">AMBER HIVE</p>
      <p class="contact__title">Title</p>
      <ul class="contact__list">
        <li class="contact__item">
          <svg class="contact__icon" viewBox="0 0 24 24" aria-hidden="true"><path d="M6.6 10.8a15.1 15.1 0 0 0 6.6 6.6l2.2-2.2a1 1 0 0 1 1-.25 11.4 11.4 0 0 0 3.6.57 1 1 0 0 1 1 1V20a1 1 0 0 1-1 1A17 17 0 0 1 3 4a1 1 0 0 1 1-1h3.5a1 1 0 0 1 1 1c0 1.25.2 2.45.57 3.57a1 1 0 0 1-.25 1z"/></svg>
          <span>+39 345 6128904</span>
        </li>
        <li class="contact__item">
          <svg class="contact__icon" viewBox="0 0 24 24" aria-hidden="true"><path d="M6.6 10.8a15.1 15.1 0 0 0 6.6 6.6l2.2-2.2a1 1 0 0 1 1-.25 11.4 11.4 0 0 0 3.6.57 1 1 0 0 1 1 1V20a1 1 0 0 1-1 1A17 17 0 0 1 3 4a1 1 0 0 1 1-1h3.5a1 1 0 0 1 1 1c0 1.25.2 2.45.57 3.57a1 1 0 0 1-.25 1z"/></svg>
          <span>+39 0431 582 6047</span>
        </li>
        <li class="contact__item">
          <svg class="contact__icon" viewBox="0 0 24 24" aria-hidden="true"><path d="M3 5h18a1 1 0 0 1 1 1v12a1 1 0 0 1-1 1H3a1 1 0 0 1-1-1V6a1 1 0 0 1 1-1zm9 7.2L4.2 7v.1L12 13l7.8-5.9V7z"/></svg>
          <span>hello@amberhive.com</span>
        </li>
      </ul>
    </div>
  </section>

</main>
</body>
</html>
```